Five Quill Voices, "Drafting and Polishing Made Bright"

We need a brochure that provides background about our company, identifies our products and services and provides our contact information. If possible, We would like the designer to use an Office suite product such as Word or Publisher to create the brochure if possible. We would like photos, color, something that inspires customers to use our services. We have attached a copy of a draft brochure and we believe the text in the brochure is good, but the brochure is cold, bland and lacks color, style and a fresh quality. We would like all text in the brochure to be included as well as the attached logo and company name somewhere on the front and back of the brochure. Please feel free to resize the logo and use creative license to develop the brochure as you please. However, the brochure colors should compliment the dark blue, light blue and black colors in the logo. Most of all, the brochure needs to be engaging, inviting, fresh and ultra professional. Thanks!

Target Market(s)

Small and large scale businesses who would use self-help books, writing services for blogs and Chatterly posts, newsletters and manuscript reviews.

Industry/Entity Type

Marketing

Font styles to use
Serif

Colors
0655a3
3377b5
85acd3
000000

Requirements
Must have
• -Logo and company name; text in draft brochure
• -Color and business photos which relate to the products/services provided
• -Inspiring, engaging, professional feel and style
• -I would like colors which compliment the logo colors (perhaps the colors below, but we are open to designer choices
• -Since this is a writing/editing business, something in the brochure that reflects that would be good.
Nice to have
• -Open; depends on the designer preference
• -Use of Office Word or Publisher program, but we are open to the use of other programs.
Should not have
• -Bland brochure with only text

```html
<!DOCTYPE html>
<html lang="en">
<head>
<meta charset="utf-8">
<title>Five Quill Voices – Brochure Inside Spread</title>
<link href="https://fonts.googleapis.com/css2?family=Libre+Baskerville:ital,wght@0,400;0,700;1,700&family=Montserrat:wght@400;500&display=swap" rel="stylesheet">
<style>
  :root {
    --ink: #1c1c1c;
    --body: #2e2e2e;
    --paper: #ffffff;
    --rule: #1a1a1a;
    --slate-top: #46494e;
    --slate-mid: #56697a;
    --steel-blue: #5f84a2;
    --deep-blue: #0655a3;
    --mid-blue: #3377b5;
    --light-blue: #85acd3;
    --on-dark: #f2f5f8;
  }
  html, body { margin: 0; padding: 0; }
  body {
    width: 1200px; height: 1200px; overflow: hidden;
    background: var(--paper); position: relative;
    font-family: "Montserrat", sans-serif; color: var(--body);
  }
  .spread { position: absolute; left: 0; top: 136px; width: 1200px; height: 926px; }
  .panel { position: absolute; top: 0; height: 926px; overflow: hidden; }
  .panel--overview { left: 0; width: 400px; background: var(--paper); }
  .panel--services { left: 400px; width: 398px; background: var(--paper); }
  .panel--writing { left: 798px; width: 402px; }
  .writing-photo { position: absolute; inset: 0;
    background: linear-gradient(180deg, var(--slate-top) 0%, var(--slate-mid) 45%, var(--steel-blue) 100%); }

  .abs { position: absolute; z-index: 1; }
  .section-title {
    font-family: "Libre Baskerville", serif; font-weight: 700; color: var(--ink);
    font-size: 17px; letter-spacing: 1px; margin: 0; white-space: nowrap;
  }
  .section-rule { position: absolute; height: 3px; background: var(--rule); }
  .sub-title {
    font-family: "Libre Baskerville", serif; font-weight: 400; color: var(--ink);
    font-size: 15px; letter-spacing: 0.8px; margin: 0; white-space: nowrap;
    text-decoration: underline; text-underline-offset: 3px; text-decoration-thickness: 1px;
  }
  .copy { font-size: 10.4px; line-height: 22.8px; margin: 0; letter-spacing: 0.1px; }
  .copy--loose { line-height: 24px; }
  .end-mark { display: inline-block; width: 7px; height: 7px; background: var(--ink); margin-left: 5px; vertical-align: 0; }
  .panel--writing .copy { color: var(--on-dark); }
  .panel--writing .sub-title { color: var(--on-dark); }
  .panel--writing .end-mark { background: var(--on-dark); }

  .values { list-style: none; margin: 0; padding: 0; }
  .values li { position: relative; padding-left: 18px; font-size: 12px; font-weight: 500;
    line-height: 24px; color: var(--ink); margin-bottom: 0.5px; }
  .values li::before { content: ""; position: absolute; left: 0; top: 8px; width: 7px; height: 7px; background: var(--ink); }

  .photo { position: absolute; }
  .photo--desk { left: 0; top: 664px; width: 400px; height: 262px;
    background: linear-gradient(180deg, #ffffff 0%, #e2e0de 30%, #b9b2ab 65%, #8d847c 100%); }
  .photo--books { left: 0; top: 178px; width: 398px; height: 180px;
    background: linear-gradient(120deg, #2c3a4a 0%, #3f6f94 45%, #7c8fa0 75%, #3b4652 100%); }
  .photo--laptop { left: 0; top: 730px; width: 398px; height: 196px;
    background: linear-gradient(135deg, #2d2a28 0%, #4a4743 40%, #6e7479 70%, #2c2f33 100%); }
  .books-label { position: absolute; left: 0; width: 398px; top: 72px; text-align: center;
    font-family: "Libre Baskerville", serif; font-style: italic; font-weight: 700; color: #fff;
    font-size: 20px; letter-spacing: 8px; }

  .slash { position: absolute; left: 0; top: 0; z-index: 1; }
  .brand { position: absolute; z-index: 1; left: 158px; top: 766px; display: flex; align-items: center; gap: 7px; }
  .brand-square { width: 18px; height: 18px; background: var(--deep-blue); }
  .brand-name { font-family: "Montserrat", sans-serif; font-size: 8.5px; font-weight: 500; color: #14253a; }
  .wordmark { position: absolute; z-index: 1; left: 0; width: 402px; top: 820px; text-align: center;
    font-family: "Montserrat", sans-serif; font-weight: 500; color: var(--on-dark);
    font-size: 17px; letter-spacing: 6px; }
</style>
</head>
<body>
<main class="spread">

  <section class="panel panel--overview">
    <div class="photo photo--desk" role="img" aria-label="Photo of hands writing and editing on printed pages, fading into white"></div>
    <h2 class="section-title abs" style="left:33px; top:24px;">Company Overview Description</h2>
    <div class="section-rule" style="left:34px; top:51px; width:233px;"></div>
    <p class="copy abs" style="left:35px; top:72px; width:300px;">
      Five Quill Voices Publications dba Five Quill Voices was founded in 2017 by Maren T. Holloway, a Social Services Administrator, author and publisher. Five Quill Voices has become a trusted name with a solid, local reputation as a small business that offers adult, trade books which focus on improving the financial and physical health of mature adults. Five Quill Voices also provides a multi-disciplinary approach to editing and writing services related to trending topics, educational, evergreen pieces or social media matters.
    </p>
    <p class="copy abs" style="left:35px; top:322px; width:300px;">
      Since early 2018, Five Quill Voices’ operations have focused on producing scalable, high-quality content solutions to meet unique business to develop content to engage audiences. At Five Quill Voices, we implemented sound organizational goals which center around our values:
    </p>
    <ul class="values abs" style="left:35px; top:478px; width:335px;">
      <li>Easy order interface complimented by excellent customer service levels.</li>
      <li>Qualified writers which provide expert editing and writing services.</li>
      <li>Engagement of targeted audiences designed to increase sales and enhance client work product.</li>
      <li>Timely deliverables with 100% satisfaction.</li>
    </ul>
  </section>

  <section class="panel panel--services">
    <h2 class="section-title abs" style="left:23px; top:28px;">Our Products &amp; Services</h2>
    <div class="section-rule" style="left:25px; top:56px; width:233px;"></div>
    <p class="copy copy--loose abs" style="left:27px; top:66px; width:340px;">
      Five Quill Voices offers a highly-focused service approach to provide adult, trade books and offer quality editing and writing services to produce blog and Chatterly posts, white papers, newsletters and manuscript reviews<span class="end-mark"></span>
    </p>

    <div class="photo photo--books" role="img" aria-label="Photo of a stack of colourful magazines and books">
      <div class="books-label">books</div>
    </div>

    <h3 class="sub-title abs" style="left:27px; top:373px;">Adult Trade Books</h3>
    <p class="copy abs" style="left:27px; top:405px; width:330px;">
      We are developing a series of books that will aid Baby Boomers and the Generation X population to develop and maintain good, financial planning practices and maintain stable emotional and physical health while aging. The first book in the series, Wellness, Wisdom and Renewal will be released in the Summer of 2018. Wellness, Wisdom and Renewal is a step-by-step guide to aging in America which includes estate planning, wills and trusts, caregiving, senior housing, and coping with the loss of a loved one<span class="end-mark"></span>
    </p>

    <h3 class="sub-title abs" style="left:30px; top:622px;">Blog and Chatterly Posts</h3>
    <p class="copy copy--loose abs" style="left:30px; top:654px; width:300px;">
      Blog posts are used to increase brand awareness in search engines and attract new website visitors with relevant, valuable content.
    </p>

    <div class="photo photo--laptop" role="img" aria-label="Photo of a person working on a laptop at a table by a window"></div>
  </section>

  <section class="panel panel--writing">
    <div class="writing-photo" role="img" aria-label="Muted blue-toned photo of hands writing in a notebook"></div>
    <svg class="slash" width="402" height="926" viewBox="0 0 402 926" aria-hidden="true">
      <line x1="138" y1="0" x2="50" y2="88" stroke="#ffffff" stroke-width="3"/>
      <line x1="94" y1="776" x2="0" y2="870" stroke="#ffffff" stroke-width="3"/>
    </svg>
    <p class="copy copy--loose abs" style="left:44px; top:126px; width:335px;">
      With client guidance, writers begin by mapping out each blog post to ensure topics, titles, keywords and formatting engage targeted audiences and support your business’ commercial goals.
    </p>
    <p class="copy copy--loose abs" style="left:44px; top:248px; width:335px;">
      A standard blog post (which is 550 to 650 words) is may be designed to devote special attention to a topic. Standard blog posts are short but are still detailed enough to be mobile and reader-friendly. The blogs. With navigational aids such as numbered lists, bullet points and headers, standard blog posts can be informative and engaging<span class="end-mark"></span>
    </p>

    <h3 class="sub-title abs" style="left:48px; top:512px;">White Papers</h3>
    <p class="copy abs" style="left:48px; top:544px; width:335px;">
      White papers are essential to establishing a brand as a trustworthy leader in a specific industry. These high-quality content papers build credibility among online audiences by demonstrating expertise and offering good lead generation opportunities through downloads from potential customers. Five Quill Voices will work with you to determine the topics that resonate most with your target audience to develop valuable, relevant content that supports business goals.<span class="end-mark"></span>
    </p>

    <div class="brand">
      <span class="brand-square"></span>
      <span class="brand-name">Five Quill Voices</span>
    </div>
    <div class="wordmark">FIVE QUILL VOICES</div>
  </section>

</main>
</body>
</html>
```